The Quiet Tide of Morning: A Path Through Silence, Courage and Light

I require designs for the front cover, rear cover and spine for a printed book. The book is the personal account of a stroke survivor.

Dimensions requested by publisher:|

Front + rear covers = 130 x 195mm with 3-5mm bleed
Spine = c. 10mm

Target Market(s)

Worldwide

Font styles to use
Decorative
Script

Requirements
Must have
• The text for the back cover (and I have attached photos for the accompanying headshot):

"Ruth Kembo had become a successful commercial lawyer in Tanzania with a professional career that spanned almost two decades. One week after celebrating her law firm’s 5th anniversary her life changed dramatically when at 4am one morning she suffered an ischaemic stroke.

After losing the use of the right side of her body and her ability to speak and swallow, Ruth was forced to undergo a full system reboot. In this brutally honest account of her life before and after the stroke Ruth describes her physical and mental battles, how she managed to accept the condition and deal with the accompanying feelings of shame.

Her story is one of rebirth, hope and ultimately transformation, offering practical advice for stroke survivors, their families and anyone embarking on a rehabilitation programme following serious illness."
Nice to have
• Modern but elegant feel. Something that signifies the metamorphosis of a butterfly, or transformation in general.

```html
<!DOCTYPE html>
<html lang="en">
<head>
<meta charset="utf-8">
<title>The Quiet Tide of Morning — Cover</title>
<link rel="stylesheet" href="https://fonts.googleapis.com/css2?family=Montserrat:wght@400;600;700&family=Tinos:wght@400;700&family=Oswald:wght@700&family=Arimo:wght@400&display=swap">
<style>
  :root {
    --paper: #ffffff;
    --ink: #111111;
    --plum: #3d0a52;
    --rose: #c2245a;
    --wing-light: #c4b698;
    --wing-mid: #9a8a6c;
    --wing-dark: #3e3a2c;
    --chrysalis: #4d6a4a;
    --shell-brown: #5a3e2c;
    --shell-teal: #1f4f5a;
  }
  html, body {
    margin: 0;
    padding: 0;
    width: 1200px;
    height: 867px;
    overflow: hidden;
    background: var(--paper);
  }
  .cover {
    position: relative;
    width: 1200px;
    height: 867px;
    background: var(--paper);
    color: var(--ink);
  }

  /* Rear cover */
  .rear-title {
    position: absolute;
    left: 0;
    width: 585px;
    top: 72px;
    margin: 0;
    text-align: center;
    font-family: "Tinos", serif;
    font-weight: 400;
    font-size: 27px;
    line-height: 32px;
    color: var(--plum);
    white-space: nowrap;
  }
  .rear-subtitle {
    position: absolute;
    left: 0;
    width: 556px;
    top: 110px;
    margin: 0;
    text-align: center;
    font-family: "Montserrat", sans-serif;
    font-weight: 400;
    font-size: 19px;
    line-height: 23px;
    letter-spacing: 0.6px;
  }
  .headshot {
    position: absolute;
    left: 229px;
    top: 175px;
    width: 94px;
    height: 94px;
  }
  .blurb {
    position: absolute;
    left: 57px;
    top: 277px;
    width: 471px;
    font-family: "Montserrat", sans-serif;
    font-size: 16.6px;
    line-height: 22.6px;
    letter-spacing: 0.6px;
  }
  .blurb p {
    margin: 0 0 22.6px;
    text-align: justify;
  }
  .blurb strong { font-weight: 700; }

  /* Spine */
  .spine-title {
    position: absolute;
    left: 585px;
    top: 60px;
    margin: 0;
    writing-mode: vertical-rl;
    white-space: nowrap;
    font-family: "Oswald", sans-serif;
    font-weight: 700;
    font-size: 26px;
    line-height: 28px;
    color: var(--plum);
  }
  .spine-author {
    position: absolute;
    left: 586px;
    top: 664px;
    margin: 0;
    writing-mode: vertical-rl;
    white-space: nowrap;
    font-family: "Montserrat", sans-serif;
    font-weight: 400;
    font-size: 26px;
    line-height: 28px;
    letter-spacing: 1px;
    color: var(--rose);
  }

  /* Front cover */
  .front-art {
    position: absolute;
    left: 627px;
    top: 0;
    width: 573px;
    height: 410px;
  }
  .front-title {
    position: absolute;
    left: 660px;
    width: 520px;
    top: 420px;
    margin: 0;
    text-align: center;
    font-family: "Tinos", serif;
    font-weight: 700;
    font-size: 55px;
    line-height: 61px;
    color: var(--plum);
    letter-spacing: 0.5px;
  }
  .front-subtitle {
    position: absolute;
    left: 660px;
    width: 520px;
    top: 664px;
    margin: 0;
    text-align: center;
    font-family: "Arimo", sans-serif;
    font-size: 29px;
    line-height: 34px;
  }
  .front-author {
    position: absolute;
    left: 660px;
    width: 520px;
    top: 774px;
    margin: 0;
    text-align: center;
    font-family: "Montserrat", sans-serif;
    font-weight: 400;
    font-size: 54px;
    line-height: 64px;
    letter-spacing: 1px;
    color: var(--rose);
    white-space: nowrap;
  }
</style>
</head>
<body>
<main class="cover">

  <section class="rear">
    <h2 class="rear-title">THE QUIET TIDE OF MORNING</h2>
    <p class="rear-subtitle">A PATH THROUGH SILENCE,<br>COURAGE AND LIGHT</p>

    <svg class="headshot" viewBox="0 0 94 94" role="img" aria-label="Author headshot of Ruth Kembo">
      <defs>
        <radialGradient id="headshot-tone" cx="50%" cy="40%" r="60%">
          <stop offset="0%" stop-color="#b9a6a0"/>
          <stop offset="65%" stop-color="#9a86a8"/>
          <stop offset="100%" stop-color="#d8d4d0"/>
        </radialGradient>
      </defs>
      <circle cx="47" cy="47" r="47" fill="url(#headshot-tone)"/>
    </svg>

    <div class="blurb">
      <p><strong>Ruth Kembo</strong> had become a successful commercial lawyer in Tanzania with a professional career that spanned almost two decades. One week after celebrating her law firm’s 5th anniversary her life changed dramatically when at 4am one morning she suffered an ischaemic stroke.</p>
      <p>After losing the use of the right side of her body and her ability to speak and swallow, Ruth was forced to undergo a full system reboot. In this brutally honest account of her life before and after the stroke Ruth describes her physical and mental battles, how she managed to accept the condition and deal with the accompanying feelings of shame.</p>
      <p>Her story is one of rebirth, hope and ultimately transformation, offering practical advice for stroke survivors, their families and anyone embarking on a rehabilitation programme following serious illness.</p>
    </div>
  </section>

  <section class="spine">
    <h2 class="spine-title">THE QUIET TIDE OF MORNING</h2>
    <p class="spine-author">RUTH KEMBO</p>
  </section>

  <section class="front">
    <svg class="front-art" viewBox="0 0 573 410" role="img" aria-label="Photograph of a butterfly emerging from its chrysalis, hanging beside empty chrysalis shells">
      <defs>
        <radialGradient id="wing-tone" cx="50%" cy="55%" r="50%">
          <stop offset="0%" stop-color="var(--wing-light)"/>
          <stop offset="60%" stop-color="var(--wing-mid)"/>
          <stop offset="85%" stop-color="var(--wing-mid)" stop-opacity="0.6"/>
          <stop offset="100%" stop-color="var(--wing-mid)" stop-opacity="0"/>
        </radialGradient>
        <radialGradient id="shell-green" cx="50%" cy="40%" r="50%">
          <stop offset="0%" stop-color="var(--chrysalis)" stop-opacity="0.85"/>
          <stop offset="70%" stop-color="var(--wing-dark)" stop-opacity="0.6"/>
          <stop offset="100%" stop-color="var(--wing-dark)" stop-opacity="0"/>
        </radialGradient>
        <radialGradient id="shell-brown" cx="50%" cy="30%" r="50%">
          <stop offset="0%" stop-color="var(--shell-brown)" stop-opacity="0.85"/>
          <stop offset="70%" stop-color="var(--shell-brown)" stop-opacity="0.5"/>
          <stop offset="100%" stop-color="var(--shell-brown)" stop-opacity="0"/>
        </radialGradient>
        <radialGradient id="shell-dark" cx="50%" cy="50%" r="50%">
          <stop offset="0%" stop-color="var(--shell-teal)"/>
          <stop offset="60%" stop-color="#151515" stop-opacity="0.85"/>
          <stop offset="100%" stop-color="#151515" stop-opacity="0"/>
        </radialGradient>
      </defs>
      <ellipse cx="130" cy="70" rx="110" ry="100" fill="url(#shell-green)"/>
      <ellipse cx="420" cy="20" rx="160" ry="60" fill="url(#shell-brown)"/>
      <ellipse cx="45" cy="290" rx="45" ry="75" fill="url(#shell-dark)"/>
      <ellipse cx="335" cy="255" rx="125" ry="160" fill="url(#wing-tone)"/>
    </svg>

    <h1 class="front-title">THE<br>QUIET TIDE<br>OF MORNING</h1>
    <p class="front-subtitle">A PATH THROUGH SILENCE,<br>COURAGE AND LIGHT</p>
    <p class="front-author">RUTH KEMBO</p>
  </section>

</main>
</body>
</html>
```